I need a business card design for my streamora channel called The Plain Kettle Show. I make streamora cooking tutorials. I'd like the phrase " I'll see you next time, for my next meal" somewhere on the BC. The Streamora web address is www.streamora.example/user/PlainKettleShow
email - promos@zentaclip.example
Updates
I have just updated what i am looking for on the card. Thanks
Industry/Entity Type
Cooking
Contact Information for Business Card
The name of my business is The Plain Kettle Show. It's a Streamora channel & the url is https://www.streamora.example/user/PlainKettleShow
Am am a StreamOra partner.
My name is Marcus.
Logo Text
The Plain Kettle Show
Logo styles of interest
Pictorial/Combination Logo
Look and feel
Each slider illustrates characteristics of the customer's brand and the style your logo design should communicate.

```html
<!DOCTYPE html>
<html lang="en">
<head>
<meta charset="utf-8">
<title>The Plain Kettle Show – Business Card</title>
<link rel="stylesheet" href="https://fonts.googleapis.com/css2?family=Oswald:wght@600&family=Questrial&display=swap">
<style>
  :root {
    --backdrop: #232323;
    --frame: #f7f7f7;
    --card-top: #474747;
    --card-bottom: #3c3c3c;
    --orange: #e3952d;
    --orange-light: #eeb565;
    --white: #ffffff;
    --soft-white: #e6e6e6;
    --ink: #3a3a3a;
    --thumb-frame: #a3a3a3;
  }
  * { box-sizing: border-box; margin: 0; padding: 0; }
  html, body { width: 1000px; height: 1200px; overflow: hidden; }
  body { background: var(--backdrop); position: relative; font-family: "Questrial", sans-serif; }

  .card {
    position: absolute;
    width: 806px; height: 466px;
    background: var(--frame);
    padding: 13px;
  }
  .card--front { left: 102px; top: 99px; }
  .card--back  { left: 104px; top: 628px; }
  .card__face {
    position: relative;
    width: 100%; height: 100%;
    background: linear-gradient(180deg, var(--card-top), var(--card-bottom));
  }

  .brand-mark {
    position: absolute;
    width: 150px; height: 150px;
    background: var(--orange);
    color: var(--white);
    font-family: "Questrial", sans-serif;
    font-size: 24px; line-height: 1.15;
    display: flex; align-items: center; justify-content: center;
    text-align: center; padding: 12px;
  }
  .card--front .brand-mark { left: 17px; top: 18px; }
  .card--back  .brand-mark { left: 315px; top: 36px; }

  .host-badge {
    position: absolute; left: 348px; top: 25px;
    width: 205px; height: 75px;
    border-radius: 18px;
    background: linear-gradient(180deg, var(--orange-light) 0%, var(--orange) 45%);
    color: var(--white);
    font-family: "Oswald", sans-serif; font-weight: 600;
    font-size: 40px; letter-spacing: 1px;
    display: flex; align-items: center; justify-content: center;
    text-shadow: 0 1px 2px rgba(0,0,0,.25);
  }

  .show-title {
    position: absolute; left: 186px; top: 128px; width: 594px;
    text-align: center;
    font-family: "Questrial", sans-serif; font-weight: 400;
    font-size: 50px; color: var(--orange); letter-spacing: 1px;
    white-space: nowrap;
  }
  .show-title .initial { font-family: "Oswald", sans-serif; font-weight: 600; }
  .show-title .word--light { color: var(--white); }

  .sign-off {
    position: absolute; left: 186px; top: 222px; width: 594px;
    text-align: center;
    font-family: "Questrial", sans-serif; font-size: 21px;
    color: var(--soft-white); letter-spacing: .5px;
    white-space: nowrap;
  }

  .dish-strip { position: absolute; left: 18px; top: 322px; }
  .dish {
    position: absolute; top: 0;
    width: 173px; height: 98px;
    border: 5px solid var(--thumb-frame);
  }
  .dish--apples  { left: 0;   background: linear-gradient(135deg, #f3f3f3, #c62a33 55%, #e8e8e8); }
  .dish--pool    { left: 189px; background: linear-gradient(180deg, #ffffff 10%, #e9e46a 40%, #d9d458); }
  .dish--rainbow { left: 379px; background: radial-gradient(circle at 50% 50%, #d5453a, #2f7bd0 35%, #000 65%); }
  .dish--candy   { left: 569px; background: linear-gradient(135deg, #9b8c7c, #5a3b2a 45%, #e2d4c1); }

  .contact-pill {
    position: absolute;
    height: 58px; border-radius: 14px;
    background: var(--white);
    display: flex; align-items: center;
    color: var(--ink); font-size: 17px;
    white-space: nowrap;
  }
  .contact-pill--channel { left: 113px; top: 217px; width: 554px; padding-left: 16px; }
  .contact-pill--mail    { left: 207px; top: 288px; width: 366px; padding-left: 14px; }
  .platform-name {
    font-family: "Questrial", sans-serif; font-size: 22px;
    color: var(--ink); margin-right: 12px;
  }
  .mail-icon { width: 52px; height: 34px; margin-right: 10px; flex: none; }
</style>
</head>
<body>

  <section class="card card--front">
    <div class="card__face">
      <div class="brand-mark">The Plain Kettle Show</div>
      <div class="host-badge">MARCUS'S</div>
      <h1 class="show-title"><span class="initial">T</span>he <span class="initial">P</span>lain <span class="word--light"><span class="initial">K</span>ettle</span> <span class="initial">S</span>how</h1>
      <p class="sign-off">“I'll see you next time, for my next meal”</p>
      <div class="dish-strip">
        <div class="dish dish--apples" role="img" aria-label="Photo of candied strawberries on sticks"></div>
        <div class="dish dish--pool" role="img" aria-label="Photo of a yellow pool-party themed cake"></div>
        <div class="dish dish--rainbow" role="img" aria-label="Photo of a rainbow layered jelly slice"></div>
        <div class="dish dish--candy" role="img" aria-label="Photo of a candy-covered surprise cake"></div>
      </div>
    </div>
  </section>

  <section class="card card--back">
    <div class="card__face">
      <div class="brand-mark">The Plain Kettle Show</div>
      <div class="contact-pill contact-pill--channel">
        <span class="platform-name">StreamOra</span>
        <span class="contact-text">https://www.streamora.example/user/PlainKettleShow</span>
      </div>
      <div class="contact-pill contact-pill--mail">
        <svg class="mail-icon" viewBox="0 0 52 34" aria-hidden="true">
          <rect x="1.5" y="1.5" width="49" height="31" fill="none" stroke="#e3952d" stroke-width="2"/>
          <polyline points="1.5,1.5 26,20 50.5,1.5" fill="none" stroke="#e3952d" stroke-width="2"/>
          <line x1="1.5" y1="32.5" x2="20" y2="15" stroke="#e3952d" stroke-width="2"/>
          <line x1="50.5" y1="32.5" x2="32" y2="15" stroke="#e3952d" stroke-width="2"/>
        </svg>
        <span class="contact-text">promos@zentaclip.example</span>
      </div>
    </div>
  </section>

</body>
</html>
```